Zanquorra Business Card Design

Zanquorra is a small and new restaurant/ bar location in Hong Kong. The name "Djibouti" derives from an African country. There is no specific reason behind other than the fact, that the bar is somewhat inspired by African elements (only inspired but not purely based on African cuisine etc.).

The bar is somewhat a fusion of African, Mediterranean and Oriental (Old French Vietnam) elements.

However, it is very imperative to stress, that the overall look and feel of Zanquorra is a very high end cocktail lounge/ bar location. The bar is tucked away in a hidden alley, so people will have to know about it. The idea is to send the consumer off in an Escape or hidden remote location where they are at ease in a hip, stylish and trendy environment.

The card needs to feel high-end.

Final logo artwork has been attached and also pictures of the bar/ restaurant itself. The logo ie monkey head cannot be modified. However, the background color and the color of the type "ZANQUORRA" can be changed.

The following details need to fit onto the business card. Of course they can be arranged to your liking:

LOGO

Colin Vey
Partner

+852 97035164
xxx@zanquorra.com
www.zanquorra.com
7C, Brennick Road, Wan Chai, Hong Kong

```html
<!DOCTYPE html>
<html lang="en">
<head>
<meta charset="utf-8">
<title>Zanquorra Business Card</title>
<link rel="stylesheet" href="https://fonts.googleapis.com/css2?family=Cinzel:wght@400;600&display=swap">
<style>
  :root {
    --backdrop: #efe9e0;
    --plum-deep: #3f1152;
    --plum-light: #7a3c96;
    --gold: #d9a640;
    --gold-pale: #fbecbf;
    --gold-rich: #e9bc4f;
    --ink: #3a0f45;
    --emblem-tint: rgba(190, 140, 60, 0.16);
    --shadow: rgba(40, 20, 10, 0.35);
  }
  * { margin: 0; padding: 0; box-sizing: border-box; }
  html, body {
    width: 1200px; height: 1000px; overflow: hidden;
    background: var(--backdrop);
  }
  .canvas { position: relative; width: 1200px; height: 1000px; }
  .card {
    position: absolute; left: 308px; width: 582px; height: 368px;
    border-radius: 9px; overflow: hidden;
    box-shadow: 0 3px 8px var(--shadow);
    font-family: "Cinzel", "Times New Roman", serif;
  }
  .card--front {
    top: 124px;
    background: radial-gradient(ellipse at 50% 45%, var(--plum-light) 0%, var(--plum-deep) 75%);
  }
  .brand-mark {
    position: absolute; left: 220px; top: 46px;
    width: 152px; height: 152px; border-radius: 50%;
    background: var(--gold);
  }
  .brand-name {
    position: absolute; left: 0; right: 0; top: 228px;
    text-align: center; font-size: 54px; font-weight: 600;
    letter-spacing: 2px; color: var(--gold);
  }
  .card--back {
    top: 520px;
    background: linear-gradient(120deg, var(--gold-rich) 0%, var(--gold-pale) 45%, var(--gold-rich) 100%);
  }
  .back-emblem {
    position: absolute; left: 135px; top: 10px;
    width: 320px; height: 320px; border-radius: 50%;
    border: 14px solid var(--emblem-tint);
  }
  .holder { position: absolute; left: 0; right: 0; text-align: center; color: var(--ink); }
  .holder-name { top: 62px; font-size: 44px; font-weight: 600; }
  .holder-role { top: 124px; font-size: 25px; font-weight: 600; }
  .contact {
    position: absolute; left: 68px; top: 210px;
    list-style: none; color: var(--ink);
    font-size: 18px; line-height: 22.5px; font-weight: 600;
  }
</style>
</head>
<body>
<main class="canvas">
  <section class="card card--front">
    <div class="brand-mark"></div>
    <div class="brand-name">ZANQUORRA</div>
  </section>
  <section class="card card--back">
    <div class="back-emblem"></div>
    <div class="holder holder-name">Colin Vey</div>
    <div class="holder holder-role">Partner</div>
    <ul class="contact">
      <li>+852 97035164</li>
      <li>xxx@zanquorra.com</li>
      <li>www.zanquorra.com</li>
      <li>7C, Brennick Road, Wan Chai, Hong Kong</li>
    </ul>
  </section>
</main>
</body>
</html>
```